依頼詳細
ダイエット効果の期待できるボディー用クリームのパッケージ(箱)のデザインです。効果が早い(時間)、スリムになる(ライン)等がイメージされるもの。箱6面の内天、正面、左面、右面のデザインをお願いします。正面、左面、右面が同じものでも構いませんし、三面で一つのデザインになっていても構いません。
正面W52mm×H148mm、左右面W38mm×H148mm、天W52mm×W38mm
記載項目
商品名「VELMORA TIDE」とNatural Herb Extractを明記。効果が早い(時間)、スリムになる(ライン)等のイメージをいれてください。
展開図のままで大丈夫です。
希望イメージ
シンプル 複雑
単色 カラフル
暗い 明るい
日常 高級
遊び心 厳粛
未来的 伝統的
女性的 男性的
希望する色
納品ファイル
• イラストレーター形式 (.ai)
補足説明
添付しました展開図のサイズが間違っていました。

```html
<!DOCTYPE html>
<html lang="en">
<head>
<meta charset="UTF-8">
<title>Velmora Tide Diet Body Cream – Box Dieline</title>
<link rel="stylesheet" href="https://fonts.googleapis.com/css2?family=Cinzel:wght@400&family=Great+Vibes&family=Cormorant+Garamond:ital,wght@0,500;1,500&display=swap">
<style>
  :root {
    --paper: #ffffff;
    --dieline: #9aa4ad;
    --ice: #e8f5fc;
    --sky: #9fd6f2;
    --azure: #3fa9e3;
    --deep: #0d6fb8;
    --silver: #8a9196;
    --script: #4a5258;
  }
  html, body { margin: 0; padding: 0; overflow: hidden; background: var(--paper); }
  .canvas { position: relative; width: 827px; height: 1200px; overflow: hidden; background: var(--paper); }

  .panel { position: absolute; box-sizing: border-box; border: 1px solid var(--dieline); overflow: hidden; }
  .panel--top   { left: 243px; top: 0;     width: 369px; height: 262px; }
  .panel--left  { left: 0;     top: 262px; width: 243px; height: 938px; }
  .panel--front { left: 243px; top: 262px; width: 369px; height: 938px; }
  .panel--right { left: 612px; top: 262px; width: 215px; height: 938px; }

  .ribbons { position: absolute; inset: 0; }
  .panel--top .ribbons {
    background:
      linear-gradient(160deg, transparent 30%, rgba(159,214,242,.7) 55%, transparent 72%),
      linear-gradient(120deg, var(--ice) 0%, var(--paper) 40%, var(--sky) 100%);
  }
  .panel--left .ribbons {
    background: linear-gradient(100deg, var(--deep) 0%, var(--azure) 22%, var(--sky) 45%, var(--ice) 70%, var(--paper) 100%);
  }
  .panel--front .ribbons {
    background:
      linear-gradient(178deg, transparent 72%, rgba(63,169,227,.85) 92%, var(--deep) 100%),
      linear-gradient(90deg, var(--azure) 0%, var(--sky) 14%, var(--ice) 35%, var(--paper) 60%, var(--ice) 85%, var(--sky) 100%);
  }
  .panel--right .ribbons {
    background:
      linear-gradient(178deg, transparent 75%, rgba(63,169,227,.7) 95%, var(--azure) 100%),
      linear-gradient(90deg, var(--sky) 0%, var(--ice) 30%, var(--paper) 55%, var(--sky) 85%, var(--azure) 100%);
  }

  .brand {
    position: absolute;
    font-family: "Cinzel", "Times New Roman", serif;
    font-weight: 400;
    color: var(--silver);
    letter-spacing: 1px;
    line-height: 1;
    margin: 0;
    white-space: nowrap;
  }
  .brand .line { display: block; }
  .tagline {
    position: absolute;
    font-family: "Great Vibes", cursive;
    color: var(--script);
    margin: 0;
    white-space: nowrap;
    line-height: 1;
  }
  .herb-badge {
    position: absolute;
    width: 92px; height: 92px;
    border-radius: 50%;
    border: 2px solid var(--silver);
    display: flex; align-items: center; justify-content: center; text-align: center;
    font-family: "Cormorant Garamond", Georgia, serif;
    font-style: italic; font-weight: 500;
    font-size: 15px; line-height: 1.1;
    color: var(--script);
    box-sizing: border-box;
  }
  .vertical { writing-mode: vertical-rl; }

  /* top flap */
  .panel--top .brand--first  { left: 70px;  top: 40px;  font-size: 40px; }
  .panel--top .brand--second { left: 200px; top: 100px; font-size: 40px; }
  .panel--top .herb-note {
    position: absolute; left: 100px; top: 106px;
    font-family: "Cormorant Garamond", Georgia, serif; font-style: italic; font-weight: 500;
    font-size: 14px; line-height: 1.1; color: var(--script); margin: 0; text-align: right;
  }
  .panel--top .tagline { left: 110px; top: 182px; font-size: 30px; }

  /* left side */
  .panel--left .herb-badge { left: 80px; top: 70px; }
  .panel--left .herb-badge span { writing-mode: vertical-rl; }
  .panel--left .brand { left: 70px; top: 300px; font-size: 46px; }
  .panel--left .tagline { left: 92px; top: 640px; font-size: 34px; }

  /* front */
  .panel--front .herb-badge { left: 138px; top: 440px; }
  .panel--front .brand { left: 0; right: 0; top: 565px; text-align: center; font-size: 50px; }
  .panel--front .tagline { left: 0; right: 0; top: 735px; text-align: center; font-size: 38px; }

  /* right side */
  .panel--right .tagline { left: 96px; top: 40px; font-size: 32px; }
  .panel--right .brand { left: 56px; top: 370px; font-size: 46px; }
  .panel--right .herb-badge { left: 62px; top: 730px; }
  .panel--right .herb-badge span { writing-mode: vertical-rl; }
</style>
</head>
<body>
<main class="canvas">

  <section class="panel panel--top" aria-label="Top flap">
    <div class="ribbons" role="img" aria-label="Flowing blue ribbon waves"></div>
    <h2 class="brand brand--first">VELMORA</h2>
    <p class="herb-note">Natural Herb<br>Extract</p>
    <h2 class="brand brand--second">TIDE</h2>
    <p class="tagline">Diet Body Cream</p>
  </section>

  <section class="panel panel--left" aria-label="Left side panel">
    <div class="ribbons" role="img" aria-label="Flowing blue ribbon waves"></div>
    <div class="herb-badge"><span>Natural Herb Extract</span></div>
    <h2 class="brand vertical"><span class="line">VELMORA</span><span class="line">TIDE</span></h2>
    <p class="tagline vertical">Diet Body Cream</p>
  </section>

  <section class="panel panel--front" aria-label="Front panel">
    <div class="ribbons" role="img" aria-label="Flowing blue ribbon waves"></div>
    <div class="herb-badge"><span>Natural<br>Herb<br>Extract</span></div>
    <h1 class="brand"><span class="line">VELMORA</span><span class="line">TIDE</span></h1>
    <p class="tagline">Diet Body Cream</p>
  </section>

  <section class="panel panel--right" aria-label="Right side panel">
    <div class="ribbons" role="img" aria-label="Flowing blue ribbon waves"></div>
    <p class="tagline vertical">Diet Body Cream</p>
    <h2 class="brand vertical"><span class="line">VELMORA</span><span class="line">TIDE</span></h2>
    <div class="herb-badge"><span>Natural Herb Extract</span></div>
  </section>

</main>
</body>
</html>
```